New Business Card Design Project

We just had our logo designed and now are in need of business cards. The new logo is attached, we would like it to be double sided, and are open to design and layouts. (Standard business card size please) Our website is currently being worked on so if you need ideas as to what we do please look at www.lumatekhaul.com as its the same type of business

Industry/Entity Type

Remediation

Contact Information for Business Card

read above and below for details

Font styles to use
Other font styles liked:
• My Logo fonts are: font name "Airstrike Regular" 2nd line font name "Nexa Bold"

Colors

Designer to choose colors to be used in the design.

Requirements
Must have
• Name: Derek Tovalski
• Title: Owner
• Address: 412 W. Marsh Commerce Rd #31 Dunmere, ME 06518
• Phone: 555-617-2839
• Email: derek@vextaprime.com
• website: www.vextaprime.com
Nice to have
• Something that explains what we do so when you look at the card you'll know. We do the following:
• - Indoor Air Quality Testing
• - Fire & Smoke Damage
• - Water Damage & Sewer Backup
• - Storm Damage
• - Mold Remediation
• - General Contracting & Remodeling

```html
<!DOCTYPE html>
<html lang="en">
<head>
<meta charset="utf-8">
<title>Harbex Restoration – Business Cards</title>
<link href="https://fonts.googleapis.com/css2?family=Montserrat:wght@600;700;800&family=Roboto:wght@300;400&display=swap" rel="stylesheet">
<style>
  :root{
    --stage:#4a4a4a;
    --stage-edge:#2b2b2b;
    --navy:#23476b;
    --orange:#e8491f;
    --white:#ffffff;
    --ink:#6b6b6b;
    --rule:#7a7a7a;
  }
  *{margin:0;padding:0;box-sizing:border-box}
  html,body{width:1200px;height:1200px;overflow:hidden}
  body{
    background:radial-gradient(circle at 50% 50%,#5e5e5e 0%,var(--stage) 45%,var(--stage-edge) 100%);
    position:relative;
    font-family:"Roboto",Arial,sans-serif;
  }
  .card{
    position:absolute;
    left:250px;
    width:700px;height:400px;
    box-shadow:0 10px 30px rgba(0,0,0,.45);
    overflow:hidden;
  }
  /* back side */
  .card--back{top:150px;background:var(--navy);color:var(--white)}
  .brand{
    position:absolute;left:0;right:0;top:150px;
    display:flex;align-items:center;justify-content:center;gap:16px;
  }
  .brand__mark{width:34px;height:34px;background:var(--orange);flex:none}
  .brand__name{
    font-family:"Montserrat",Arial,sans-serif;font-weight:800;
    font-size:38px;letter-spacing:1px;text-transform:uppercase;
  }
  .card--back .brand__name{color:var(--white)}
  .back__web{
    position:absolute;left:0;right:0;bottom:34px;text-align:center;
    font-family:"Montserrat",Arial,sans-serif;font-weight:600;font-size:16px;letter-spacing:.5px;
  }
  .back__web .accent{color:var(--orange);font-weight:800}

  /* front side */
  .card--front{top:630px;background:var(--white)}
  .card--front .brand{
    left:50px;right:auto;top:58px;justify-content:flex-start;gap:12px;
  }
  .card--front .brand__mark{width:28px;height:28px}
  .card--front .brand__name{color:var(--orange);font-size:30px}
  .person{position:absolute;right:60px;top:170px;text-align:right}
  .person__name{
    font-family:"Montserrat",Arial,sans-serif;font-weight:800;
    font-size:24px;color:var(--orange);text-transform:uppercase;letter-spacing:.5px;
  }
  .person__title{
    font-family:"Montserrat",Arial,sans-serif;font-weight:600;
    font-size:17px;color:var(--navy);margin-top:2px;
  }
  .tab{position:absolute;right:0;top:176px;width:12px;height:44px;background:var(--navy)}
  .rule{position:absolute;left:50px;right:50px;top:250px;height:1px;background:var(--rule)}
  .contact{position:absolute;left:50px;top:266px;list-style:none}
  .contact li{
    display:flex;align-items:center;gap:8px;
    font-size:16px;font-weight:300;color:var(--ink);line-height:24px;
  }
  .contact svg{width:13px;height:13px;flex:none}
  .address{
    position:absolute;right:50px;bottom:40px;text-align:right;
    font-size:17px;font-weight:300;color:var(--ink);line-height:24px;
  }
</style>
</head>
<body>

  <section class="card card--back" aria-label="Card back">
    <div class="brand">
      <span class="brand__mark"></span>
      <span class="brand__name">Harbex Restoration</span>
    </div>
    <p class="back__web">www.<span class="accent">vextaprime</span>.com</p>
  </section>

  <section class="card card--front" aria-label="Card front">
    <div class="brand">
      <span class="brand__mark"></span>
      <span class="brand__name">Harbex Restoration</span>
    </div>

    <div class="person">
      <p class="person__name">Derek Tovalski</p>
      <p class="person__title">Owner</p>
    </div>
    <span class="tab"></span>

    <div class="rule"></div>

    <ul class="contact">
      <li>
        <svg viewBox="0 0 24 24" aria-hidden="true"><path fill="#23476b" d="M6.6 10.8a15.1 15.1 0 0 0 6.6 6.6l2.2-2.2a1 1 0 0 1 1-.25 11.4 11.4 0 0 0 3.6.57 1 1 0 0 1 1 1V20a1 1 0 0 1-1 1A17 17 0 0 1 3 4a1 1 0 0 1 1-1h3.5a1 1 0 0 1 1 1c0 1.25.2 2.45.57 3.57a1 1 0 0 1-.25 1z"/></svg>
        555-617-2839
      </li>
      <li>
        <svg viewBox="0 0 24 24" aria-hidden="true"><rect x="2" y="5" width="20" height="14" rx="1" fill="#23476b"/><path d="M2 6l10 7 10-7" fill="none" stroke="#fff" stroke-width="1.6"/></svg>
        derek@vextaprime.com
      </li>
      <li>
        <svg viewBox="0 0 24 24" aria-hidden="true"><circle cx="12" cy="12" r="10" fill="none" stroke="#23476b" stroke-width="2"/><path d="M2 12h20M12 2c3 3 3 17 0 20M12 2c-3 3-3 17 0 20" fill="none" stroke="#23476b" stroke-width="1.6"/></svg>
        www.vextaprime.com
      </li>
    </ul>

    <p class="address">412 W. Marsh Commerce Rd #31<br>Dunmere, ME 06518</p>
  </section>

</body>
</html>
```